Fun, challenging, and inspirational guide for life change - written by a coach, therapist and founde

I need (1) cover design for a book titled:
"THE HEART'S TOOLKIT FOR WORLD-BENDING IDEAS" - the unexpectedly useful craft of trusting yourself and stepping forward

A 2ND COVER will be need for a companion ebook, titled:
"THE HEART'S FIELD MANUAL FOR THRIVING AND JOY - 4 moves to open up and set free the boundless self by embracing your edges

These books will be used to promote a larger suite of products and services devoted to empowering and inspiring a community of OVERCOMERS.

For reference check out www.lanternmakershall.example

I've included some photos for visual reference points.

DESIGNS CONCEPTS:
CLEAN - A BLEND OF PAST AND PRESENT - MODERN AND THE SACRED) (...The Walcott Almanac meets

Target Market(s)

young and aspiring professionals and seasoned pros looking for life-changes due to feeling unfulfilled in their profession and relationships

Industry/Entity Type

Life Coaching

Font styles to use
Serif
Sans Serif

Requirements
Must have
• CREATIVITY - ORIGINALITY - WICKEDLY CLEAN DESIGN- AND IMPACTFUL TRANSLATION OF BRAND CONCEPT - COLOR AND PUNCH
Nice to have
• I included some photos as reference point - **PLEASE SEE THE PHOTOS FOR THE ROAD-ROVERS DESIGNS** - I really like the feeling they provoke - I want to give the viewer a sense of the journey that can be taken when they dive into these books.
• Basically, riff off the design profiles and colors included in the ROAD-ROVER covers.
• MUSTS INCLUDE -
• -ORIGINALITY
• - IMPACT
• - COLOR
• - ORIGINAL DESIGNS+
• +
Should not have
• STAY AWAY FROM...
• 1 OVERUSED AND TRENDY ICONS
• - ESOTERIC IMAGES
• - FLOWERY SCRIPTS
• - I AM REALLY LOOKING FOR A UPDATE OF THE TYPICAL SELF-HELP BOOK COVERS WHICH RELY TOO MUCH ON FLOWERY AND SACRED IMAGERY
• THANK YOU - feel free to unleash your creativity!

```html
<!DOCTYPE html>
<html lang="en">
<head>
<meta charset="utf-8">
<title>The Heart's Toolkit &amp; Field Manual — Book Covers</title>
<link rel="stylesheet" href="https://fonts.googleapis.com/css2?family=Cinzel:wght@400&family=Crimson+Pro:wght@400&display=swap">
<style>
  :root {
    --page: #ffffff;
    --frame: #3a3a3a;
    --plum-top: #604d62;
    --plum-bottom: #432d45;
    --teal-top: #64a09e;
    --teal-bottom: #387c7b;
    --ink-light: #ffffff;
    --spine-edge: #1f1f1f;
  }
  html, body { margin: 0; padding: 0; overflow: hidden; }
  body { width: 1200px; height: 1200px; background: var(--page); }
  .canvas {
    position: relative; width: 1200px; height: 1200px;
    box-sizing: border-box; border: 1.5px solid var(--frame);
    background: var(--page); overflow: hidden;
  }
  .spine, .cover { position: absolute; top: 193px; height: 815px; box-sizing: border-box; }
  .spine { width: 55px; border: 1.5px solid var(--spine-edge); }
  .cover { width: 501px; }
  .book--plum .spine, .book--plum .cover { background: linear-gradient(180deg, var(--plum-top) 0%, var(--plum-top) 55%, var(--plum-bottom) 100%); }
  .book--teal .spine, .book--teal .cover { background: linear-gradient(180deg, var(--teal-top) 0%, var(--teal-top) 55%, var(--teal-bottom) 100%); }
  .book--plum .spine { left: 16px; }
  .book--plum .cover { left: 84px; }
  .book--teal .spine { left: 611px; }
  .book--teal .cover { left: 682px; }
  .cover__hinge {
    position: absolute; top: 0; bottom: 0; left: 10px; width: 16px;
    background: linear-gradient(90deg, rgba(0,0,0,0) 0%, rgba(0,0,0,0.12) 50%, rgba(0,0,0,0) 100%);
  }
  .cover__emblem {
    position: absolute; left: 270px; top: 160px; width: 290px; height: 270px;
    transform: translateX(-50%);
    border-radius: 50%;
    background: radial-gradient(circle at 50% 50%, rgba(255,255,255,0.55) 0%, rgba(255,255,255,0.25) 35%, rgba(255,255,255,0.06) 62%, rgba(255,255,255,0) 72%);
  }
  .spine__emblem {
    position: absolute; left: 2px; right: 2px; top: 40px; height: 110px;
    background: radial-gradient(ellipse at 50% 50%, rgba(255,255,255,0.6) 0%, rgba(255,255,255,0.15) 55%, rgba(255,255,255,0) 75%);
  }
  .cover__text {
    position: absolute; left: 78px; right: 24px; top: 488px;
    color: var(--ink-light);
  }
  .book--teal .cover__text { left: 80px; top: 494px; }
  .title {
    margin: 0; font-family: "Cinzel", serif; font-weight: 400;
    letter-spacing: 0.3px; white-space: nowrap;
  }
  .title__kicker { display: block; font-size: 26px; line-height: 26px; }
  .title__lead { display: block; font-size: 34px; line-height: 34px; }
  .title__key { display: block; font-size: 72px; line-height: 62px; }
  .subtitle {
    margin: 6px 0 0; font-family: "Crimson Pro", serif; font-weight: 400;
  }
  .book--plum .subtitle { font-size: 24px; line-height: 26px; }
  .book--teal .subtitle { font-size: 18.5px; line-height: 22px; }
  .star-mark {
    position: absolute; left: 0; right: 0;
    text-align: center; color: var(--ink-light); line-height: 1;
    font-family: "Crimson Pro", serif;
  }
  .cover .star-mark { top: 722px; font-size: 30px; letter-spacing: 4px; }
  .spine .star-mark { top: 722px; font-size: 28px; }
  .book--teal .spine .star-mark { top: 686px; line-height: 1.25; }
</style>
</head>
<body>
<main class="canvas">

  <section class="book book--plum" aria-label="The Heart's Toolkit for World-Bending Ideas">
    <div class="spine">
      <div class="spine__emblem" role="img" aria-label="Small engraved brain on compass emblem"></div>
      <div class="star-mark" aria-hidden="true">★</div>
    </div>
    <div class="cover">
      <div class="cover__hinge"></div>
      <div class="cover__emblem" role="img" aria-label="Engraved brain above an open book on a compass star with scattered sparkles"></div>
      <div class="cover__text">
        <h1 class="title">
          <span class="title__kicker">THE HEART'S TOOLKIT</span>
          <span class="title__lead">FOR WORLD-BENDING</span>
          <span class="title__key">IDEAS</span>
        </h1>
        <p class="subtitle">The unexpectedly useful craft of trusting yourself and stepping forward</p>
      </div>
      <div class="star-mark" aria-hidden="true">★</div>
    </div>
  </section>

  <section class="book book--teal" aria-label="The Heart's Field Manual for Thriving and Joy">
    <div class="spine">
      <div class="spine__emblem" role="img" aria-label="Small engraved butterfly on compass emblem"></div>
      <div class="star-mark" aria-hidden="true">★<br>★</div>
    </div>
    <div class="cover">
      <div class="cover__hinge"></div>
      <div class="cover__emblem" role="img" aria-label="Engraved butterfly above an open book on a compass star with scattered sparkles"></div>
      <div class="cover__text">
        <h1 class="title">
          <span class="title__kicker">THE HEART'S FIELD MANUAL</span>
          <span class="title__lead">FOR THRIVING AND</span>
          <span class="title__key">JOY</span>
        </h1>
        <p class="subtitle">4 moves to open up and set free the boundless self by embracing your edges</p>
      </div>
      <div class="star-mark" aria-hidden="true">★★</div>
    </div>
  </section>

</main>
</body>
</html>
```